Law firm business card

Information:

Me Miriam Dufresne

website: dufresne-law.ca
email: miriam@dufresne-law.ca
Phone: 514 555-0147
Fax: 514 555-0183

Address:
Dufresne and associates
2719 Belcourt
Montreal, QC
H2K 3M9

Areas of Expertise:
Franchise Agreements, Financing, Acquisition, Real Estate Development, Commercial Agreements and Corporate Law

Target Market(s)

executives, companie managers

Industry/Entity Type

Business

Colors
f78f20
000000

Requirements
Must have
• Must use the logo, the logo is available here:

https://www.filebinder-example.com/sh/qxt8rr2ka41wpe/BBKtm7Lwzve_pQRYdNG_HJcWb

```html
<!DOCTYPE html>
<html lang="en">
<head>
<meta charset="utf-8">
<title>Dufresne &amp; Associates – Business Card</title>
<link href="https://fonts.googleapis.com/css2?family=Arimo:wght@400;700&display=swap" rel="stylesheet">
<style>
  :root {
    --orange: #f78f20;
    --black: #000000;
    --ink: #1a1a1a;
    --white: #ffffff;
    --stage: #f1ede6;
    --band-line: #f6a04a;
  }
  * { box-sizing: border-box; margin: 0; padding: 0; }
  html, body { width: 1200px; height: 960px; overflow: hidden; }
  body {
    background: var(--stage);
    font-family: "Arimo", Arial, sans-serif;
    position: relative;
  }
  .card {
    position: absolute;
    left: 250px;
    width: 700px;
    height: 400px;
    box-shadow: 0 6px 18px rgba(0,0,0,.12);
    overflow: hidden;
  }
  /* Back side */
  .card--back { top: 40px; background: var(--orange); }
  .ribbon {
    position: absolute;
    left: 0; right: 0;
    top: 95px;
    height: 130px;
    background: var(--white);
    display: flex;
    align-items: center;
    justify-content: center;
    gap: 22px;
  }
  .ribbon::before, .ribbon::after {
    content: "";
    position: absolute;
    left: 40px; right: 40px;
    height: 2px;
    background: var(--band-line);
  }
  .ribbon::before { top: 10px; }
  .ribbon::after { bottom: 10px; }
  .ribbon__mark {
    width: 64px; height: 64px;
    border: 3px solid var(--ink);
    border-radius: 50%;
  }
  .ribbon__divider { width: 2px; height: 76px; background: var(--ink); }
  .ribbon__name {
    color: var(--ink);
    font-weight: 700;
    font-size: 36px;
    letter-spacing: 2px;
    text-transform: uppercase;
    line-height: 1;
  }

  /* Front side */
  .card--front { top: 520px; display: flex; }
  .front__brand {
    width: 320px;
    background: var(--white);
    padding: 44px 0 0 40px;
  }
  .brand-mark {
    display: flex;
    flex-direction: column;
    align-items: center;
    width: 200px;
    margin-left: 20px;
  }
  .brand-mark__circle {
    width: 140px; height: 140px;
    border: 5px solid var(--orange);
    border-radius: 50%;
  }
  .brand-mark__name {
    margin-top: 12px;
    color: var(--orange);
    font-weight: 700;
    font-size: 17px;
    white-space: nowrap;
  }
  .address {
    margin-top: 28px;
    font-style: normal;
    font-size: 19px;
    line-height: 1.12;
    color: var(--ink);
  }
  .front__details {
    flex: 1;
    background: var(--orange);
    padding: 40px 36px 0 40px;
    color: var(--white);
  }
  .person-name {
    font-weight: 700;
    font-size: 32px;
    line-height: 1.05;
    text-transform: uppercase;
    text-align: center;
    letter-spacing: 1px;
    margin-bottom: 22px;
  }
  .contact-list { list-style: none; }
  .contact-list li {
    display: flex;
    align-items: center;
    gap: 12px;
    font-size: 15px;
    line-height: 1;
    margin-bottom: 11px;
  }
  .contact-list svg { width: 15px; height: 15px; flex: none; fill: var(--white); }
  .expertise { margin-top: 26px; color: var(--black); }
  .expertise__title { font-weight: 700; font-size: 12px; margin-bottom: 14px; }
  .expertise__list { font-weight: 700; font-size: 12px; line-height: 1.2; }
</style>
</head>
<body>

<section class="card card--back" aria-label="Card back">
  <div class="ribbon">
    <span class="ribbon__mark"></span>
    <span class="ribbon__divider"></span>
    <span class="ribbon__name">Dufresne &amp; Associates</span>
  </div>
</section>

<section class="card card--front" aria-label="Card front">
  <div class="front__brand">
    <div class="brand-mark">
      <span class="brand-mark__circle"></span>
      <span class="brand-mark__name">Dufresne &amp; Associates</span>
    </div>
    <address class="address">
      Dufresne &amp; Associates<br>
      2719 Belcourt<br>
      Montreal, QC<br>
      H2K 3M9
    </address>
  </div>

  <div class="front__details">
    <h1 class="person-name">Miriam<br>Dufresne</h1>
    <ul class="contact-list">
      <li>
        <svg viewBox="0 0 16 16" aria-hidden="true"><path d="M1 2h14v9H1z M3 4v5h10V4z M6 12h4v1h2v1H4v-1h2z" fill-rule="evenodd"/></svg>
        dufresne-law.ca
      </li>
      <li>
        <svg viewBox="0 0 16 16" aria-hidden="true"><path d="M1 3h14v10H1z M2.5 4.5 8 9l5.5-4.5v-.1H2.5z" fill-rule="evenodd"/></svg>
        email: miriam@dufresne-law.ca
      </li>
      <li>
        <svg viewBox="0 0 16 16" aria-hidden="true"><path d="M4 1l2.5 3-1.5 2c1 2 3 4 5 5l2-1.5 3 2.5-2 2.5C7 14 2 9 1.5 3.5z"/></svg>
        (514) 555-0147
      </li>
      <li>
        <svg viewBox="0 0 16 16" aria-hidden="true"><path d="M4 1h8v4H4z M1 6h14v6h-3v3H4v-3H1z M5 10v4h6v-4z" fill-rule="evenodd"/></svg>
        (514) 555-0183
      </li>
    </ul>
    <div class="expertise">
      <p class="expertise__title">Areas of Expertise:</p>
      <p class="expertise__list">Franchise Agreements, Financing, Acquisition<br>Real Estate Development, Commercial Agreements<br>and Corporate Law</p>
    </div>
  </div>
</section>

</body>
</html>
```